out of the box Business Card Design for a Manufacturer / Distributor

We are a manufarturer and distributor of products.
the company name is VORTANI (Pic attached)

the picture is NOT a must have on the business Card.

the Business Card should look really professional and/or special, so out of the box thinking is welcome.

there should be 2 Adresses on the Business Card for Main and Branch Office.
Email Adress, homepage, Name is required
NO Phone Number

Our working field:
Private Labeling
high Quality Production
direct distribution
warehousing
trademark registration
legal support

Main Office:
Kornblumenweg 14
08352 Haselbrück
Germany

Branch Office:
Daska Lane
Zarnabad
Pakistan

Names:
Lukas Feldhaus (Owner)
Imran Qureshi (Owner)

Email:
lukas@vortani-example.com
imran@vortani-example.com

homepage:
vortani-example.com

Industry/Entity Type

Manufacturer Distributer

Contact Information for Business Card

Vortani

Requirements
Must have
• Names, both office Adresses, email, homepage
Should not have
• Phone Number

```html
<!DOCTYPE html>
<html lang="en">
<head>
<meta charset="utf-8">
<title>Vortani Business Card</title>
<link href="https://fonts.googleapis.com/css2?family=Poppins:wght@300;400;700&display=swap" rel="stylesheet">
<style>
  :root {
    --page: #c9c9c9;
    --card-dark: #1f1f1f;
    --card-mid: #2b2a2a;
    --card-band: #302f2f;
    --white: #ffffff;
    --muted: #8a8a8a;
    --rule: #4a4a4a;
  }
  * { margin: 0; padding: 0; box-sizing: border-box; }
  html, body { width: 1200px; height: 825px; overflow: hidden; }
  body {
    background: var(--page);
    font-family: "Poppins", sans-serif;
    color: var(--white);
    position: relative;
  }
  .card {
    position: absolute;
    width: 540px;
    height: 309px;
    background: var(--card-dark);
    overflow: hidden;
    box-shadow: 0 14px 30px rgba(0,0,0,0.25);
  }
  .card-front { left: 40px; top: 258px; }
  .card-back { left: 620px; top: 258px; }

  /* front */
  .front-band {
    position: absolute; left: 0; right: 0; top: 88px; height: 142px;
    background: var(--card-band);
  }
  .edge-tab { position: absolute; width: 22px; background: var(--white); }
  .edge-tab-left { left: 0; top: 150px; height: 140px; border-radius: 0 14px 14px 0; }
  .edge-tab-right { right: 0; top: 22px; height: 140px; border-radius: 14px 0 0 14px; }
  .front-brand {
    position: absolute; left: 0; right: 0; top: 118px;
    display: flex; align-items: center; justify-content: center; gap: 14px;
  }
  .brand-dot { width: 46px; height: 46px; border-radius: 50%; background: var(--white); }
  .front-name { font-weight: 400; font-size: 50px; letter-spacing: 2px; line-height: 1; }
  .front-url {
    position: absolute; left: 50%; top: 244px; transform: translateX(-50%);
    border: 1.5px solid var(--white); border-radius: 16px;
    padding: 3px 22px; font-size: 15px; font-weight: 400; letter-spacing: 1px;
    white-space: nowrap;
  }

  /* back */
  .back-panel {
    position: absolute; left: 250px; top: 0; right: 18px; bottom: 0;
    background: var(--card-mid);
  }
  .back-brand {
    position: absolute; left: 0; width: 226px; top: 120px;
    display: flex; flex-direction: column; align-items: center; gap: 14px;
  }
  .back-brand .brand-dot { width: 56px; height: 56px; }
  .back-name-mark { font-size: 30px; font-weight: 400; letter-spacing: 1.5px; }
  .icon-strip {
    position: absolute; left: 222px; top: 128px; width: 28px; bottom: 0;
    background: var(--white); border-radius: 14px 14px 0 0;
    display: flex; flex-direction: column; align-items: center;
    padding-top: 22px; gap: 25px;
  }
  .icon-strip svg { width: 13px; height: 13px; fill: var(--card-dark); }
  .person-tab {
    position: absolute; left: 462px; top: 0; width: 32px; height: 82px;
    background: var(--white); border-radius: 0 0 16px 16px;
    display: flex; align-items: flex-end; justify-content: center; padding-bottom: 24px;
  }
  .person-tab svg { width: 15px; height: 15px; fill: var(--card-dark); }
  .holder { position: absolute; left: 270px; top: 86px; }
  .holder-name { font-size: 21px; font-weight: 700; line-height: 1.1; }
  .holder-role { font-size: 13px; color: var(--muted); font-weight: 400; margin-top: 2px; }
  .holder-role::after {
    content: ""; display: block; width: 44px; height: 2px; background: var(--white); margin-top: 3px;
  }
  .contact-list { position: absolute; left: 268px; top: 146px; width: 240px; list-style: none; }
  .contact-list li {
    font-size: 10.5px; font-weight: 300; line-height: 1.3;
    border-top: 1px solid var(--rule); padding: 4px 0 5px;
  }
  .contact-list li:last-child { border-bottom: 1px solid var(--rule); }
</style>
</head>
<body>

<section class="card card-front">
  <div class="front-band"></div>
  <div class="edge-tab edge-tab-left"></div>
  <div class="edge-tab edge-tab-right"></div>
  <div class="front-brand">
    <span class="brand-dot"></span>
    <span class="front-name">VORTANI</span>
  </div>
  <div class="front-url">www.vortani-example.com</div>
</section>

<section class="card card-back">
  <div class="back-panel"></div>
  <div class="back-brand">
    <span class="brand-dot"></span>
    <span class="back-name-mark">VORTANI</span>
  </div>
  <div class="icon-strip">
    <svg viewBox="0 0 16 16" aria-hidden="true"><path d="M1 7l14-6-5 14-2-6z"/></svg>
    <svg viewBox="0 0 16 16" aria-hidden="true"><path d="M8 1l7 7h-2v7h-4v-4H7v4H3V8H1z"/></svg>
    <svg viewBox="0 0 16 16" aria-hidden="true"><path d="M8 1l7 7h-2v7h-4v-4H7v4H3V8H1z"/></svg>
    <svg viewBox="0 0 16 16" aria-hidden="true"><path d="M8 0a8 8 0 100 16A8 8 0 008 0zm0 2a6 6 0 110 12A6 6 0 018 2z"/><path d="M2 8h12v1H2zM7.5 2h1v12h-1z"/></svg>
  </div>
  <div class="person-tab">
    <svg viewBox="0 0 16 16" aria-hidden="true"><circle cx="8" cy="5" r="3.5"/><path d="M1 16c0-4 3-6 7-6s7 2 7 6z"/></svg>
  </div>
  <div class="holder">
    <div class="holder-name">Lukas Feldhaus</div>
    <div class="holder-role">Owner</div>
  </div>
  <ul class="contact-list">
    <li>lukas@vortani-example.com</li>
    <li>Kornblumenweg 14 08352 Haselbrück<br>Germany</li>
    <li>Daska Lane Zarnabad Pakistan</li>
    <li>www.@vortani-example.com</li>
  </ul>
</section>

</body>
</html>
```